NOTE: I have uploaded a photo of my business card for reference, please use the same font on the business card for this brochure. Main colours to use - green, white, grey & black.

I would like a tri-fold brochure. At the top on the front page, I would like my "Korvel's Electrical & Solar" logo. At the bottom of the front page, please use the picture of me standing infront of the van. Please put these details on the front page: my name: "Owen Korvel" my phone number: "0491 637 158" "24/7 Emergency Service" "FREE QUOTES" "Lic No. 582614D" "ABN: 41 927 506 318". Please highlight in green (same green as my logo) "FREE QUOTES" & "24/7 Emergency Service".

On the back page, have my "S" logo at the top. Underneath, have "CONTACT". Then underneath "CONTACT" have my phone number "0491 637 158". Under my phone number, please add my email "owen@korvelpowerworks.example". I want to add my linktree QR Code so please put that at the bottom of the backpage. This QR Code links to my social media. If you can make the back page look any better, please do so.

On the page that you flick over to from the front page. Please put "OUR SERVICES". Under "OUR SERVICES", please list the following.
- LED LIGHTING UPGRADES
- SWITCHES & OUTLETS
- SMOKE ALARMS
- FAULT FINDING
- REWIRING
- SWITCHBOARD UPGRADES
- DATA/TV CABLING
- NEW BUILDS
- BATHROOM/KITCHEN/LAUNDRY RENOVATIONS
- TEST & TAGGING
- ALL ELECTRICAL MAINTENANCE & REPAIRS.
Also add a photo on this page from one of the following i have uploaded that showcases our work.

Next to the previous page in the middle pamphlet, please put. "Licensed & Insured". Under that, please have the following:
- FAST RESPONSE TIME
- TRANSPARENT PRICING, NO HIDDEN FEES
- QUALITY WORKMANSHIP GUARANTEED
- 24/7 EMERGENCY SERVICE
- TRUSTED BY THE LOCAL COMMUNITY

On the right side of the previous page: Please use this page to showcase our google reviews. I will attach 3 reviews written by our customers below. Please write the customers name below the review and put 5 gold stars above the review.

"We recently hired Korvels Electrical and Solar. Great communication throughout quoting and prompt response when engaging to commence work. Workmanship and attention to detail A1."
We have found our sparky!"
Bernard

"Owen was fantastic! He quickly solved a big problem for me and was extremely punctual, polite, and patient in answering all my questions. He identified the issue straight away, fixed it efficiently, and even gave me valuable advice for the future. I feel very lucky to have found him and would highly recommend his services!"
Mira

"By far the best in the business. The most professional and reliable service I have received. If you’re looking for a knowledgeable and experienced service I would highly recommend to anyone."
Felicity

Now there should be one page left. On this page, you can just fill the page up with images of our work that i have uploaded. Thank you so much for your time and i look forward to seeing your work! :)

Colors
59FF00
82FF00
B8FF75
E3FFCB
F4FFEA

Requirements
Must have
• Must stand out and be eye appealing.

```html
<!DOCTYPE html>
<html lang="en">
<head>
<meta charset="utf-8">
<title>Korvel's Electrical &amp; Solar – Tri-fold Brochure</title>
<link href="https://fonts.googleapis.com/css2?family=Montserrat:wght@400;500;600;700;800&display=swap" rel="stylesheet">
<style>
  :root {
    --stage: #8c8c8c;
    --panel: #1c1c1c;
    --panel-deep: #121212;
    --green: #3dba47;
    --green-bright: #52cf4d;
    --green-dark: #1f8f34;
    --white: #ffffff;
    --grey-text: #d9d9d9;
    --photo-blue: #2b4a78;
    --photo-warm: #b89460;
  }
  * { box-sizing: border-box; margin: 0; padding: 0; }
  html, body { width: 891px; height: 1200px; overflow: hidden; background: var(--stage); }
  body { font-family: "Montserrat", Arial, sans-serif; color: var(--white); }

  .stage { width: 960px; height: 1293px; transform: scale(0.928125); transform-origin: 0 0; position: relative; }

  .spread {
    position: absolute; left: 66px; width: 826px; height: 584px;
    background: var(--panel); overflow: hidden;
    box-shadow: 4px 6px 10px rgba(0,0,0,0.45);
  }
  .spread--outside { top: 50px; }
  .spread--inside { top: 668px; }

  /* ---------- Outside ---------- */
  .brand-mark {
    position: absolute; left: 306px; top: 150px; width: 216px;
    text-align: center;
  }
  .brand-mark__dot {
    width: 96px; height: 96px; border-radius: 50%;
    background: var(--green); margin: 0 auto 18px;
  }
  .brand-mark__name {
    font-weight: 800; font-size: 22px; line-height: 1.2; color: var(--white);
  }

  .contact-block { position: absolute; left: 264px; width: 300px; top: 430px; text-align: center; }
  .contact-icons { display: flex; justify-content: center; gap: 8px; margin-bottom: 14px; }
  .contact-icons svg { width: 14px; height: 14px; }
  .contact-block p { font-weight: 700; font-size: 11.5px; line-height: 15px; }
  .social-line {
    position: absolute; left: 264px; width: 300px; top: 533px;
    display: flex; justify-content: center; align-items: center; gap: 4px;
    font-size: 11.5px; color: var(--green-bright);
  }
  .social-line__dot { width: 12px; height: 12px; border-radius: 50%; background: var(--green-bright); }

  .front-panel { position: absolute; left: 551px; top: 0; width: 275px; height: 584px; }
  .front-panel__logo {
    position: absolute; top: 40px; left: 0; width: 275px; text-align: center;
    font-weight: 800; font-size: 19px; color: var(--green-bright);
  }
  .photo {
    position: absolute;
  }
  .front-panel__photo {
    left: 0; top: 93px; width: 275px; height: 298px;
    background: linear-gradient(135deg, #e8e8e8 0%, #c9ced6 40%, var(--photo-blue) 75%, #e07a2f 100%);
  }
  .emergency {
    position: absolute; left: 40px; top: 408px; display: flex; align-items: center; gap: 4px;
  }
  .emergency svg { width: 92px; height: 66px; }
  .emergency__text { line-height: 1; }
  .emergency__hours { font-weight: 800; font-style: italic; font-size: 30px; color: var(--white); }
  .emergency__label { font-weight: 700; font-size: 17px; color: var(--green-bright); margin-top: 2px; }
  .free-quotes {
    position: absolute; left: 0; top: 480px; width: 275px; height: 38px;
    background: var(--green); display: flex; align-items: center; justify-content: center;
    font-weight: 800; font-size: 23px; letter-spacing: 0.5px; color: var(--panel-deep);
  }
  .credentials {
    position: absolute; left: 18px; top: 536px; width: 245px;
    display: flex; justify-content: space-between; font-size: 12px; line-height: 14px;
  }
  .credentials .label { color: var(--green-bright); font-weight: 600; }

  /* ---------- Inside ---------- */
  .inside-header {
    position: absolute; left: 0; top: 0; width: 551px; height: 103px;
    background: linear-gradient(90deg, var(--green-dark) 0%, var(--green) 45%, #62d65a 75%, var(--green) 100%);
  }
  .inside-header h2 { position: absolute; font-weight: 700; font-size: 24px; line-height: 31px; letter-spacing: 0.3px; }
  .inside-header .services-title { left: 27px; top: 33px; }
  .inside-header .licensed-title { left: 264px; width: 300px; top: 33px; text-align: center; }

  .work-photo {
    left: 0; top: 232px; width: 551px; height: 352px;
    background: radial-gradient(ellipse at 65% 60%, var(--photo-warm) 0%, #5a5a5a 35%, var(--photo-blue) 65%, var(--panel) 100%);
    opacity: 0.85;
  }
  .work-photo__fade {
    position: absolute; left: 0; top: 232px; width: 551px; height: 140px;
    background: linear-gradient(180deg, var(--panel) 0%, rgba(28,28,28,0) 100%);
  }

  .service-list {
    position: absolute; left: 26px; top: 128px; list-style: none;
    font-size: 11px; line-height: 21.6px;
  }
  .service-list li::before { content: "• "; }

  .promise-list {
    position: absolute; left: 264px; width: 300px; top: 128px; list-style: none;
    text-align: center; font-size: 11px; line-height: 21.6px; color: var(--grey-text);
  }

  .reviews {
    position: absolute; left: 551px; top: 0; width: 275px; height: 584px;
    background: var(--panel-deep); text-align: center;
  }
  .review { position: absolute; left: 10px; width: 255px; }
  .review blockquote { font-size: 10.4px; font-weight: 600; line-height: 13px; }
  .review cite { display: block; font-style: normal; color: var(--green-bright); font-size: 11px; margin-top: 12px; }
  .review--one { top: 46px; }
  .review--two { top: 182px; }
  .review--three { top: 357px; }
  .reviews__logo {
    position: absolute; left: 0; top: 507px; width: 275px;
    font-weight: 800; font-size: 19px; color: var(--green-bright);
  }
</style>
</head>
<body>
<div class="stage">

  <section class="spread spread--outside">
    <div class="brand-mark">
      <div class="brand-mark__dot"></div>
      <div class="brand-mark__name">Korvel's Electrical &amp; Solar</div>
    </div>

    <div class="contact-block">
      <div class="contact-icons">
        <svg viewBox="0 0 16 16" aria-hidden="true"><path d="M4 1.5l2.2 3-1.4 1.6c.9 2 2.3 3.4 4.3 4.3l1.6-1.4 3 2.2-1 2.6C7.5 13.5 2.5 8.5 1.4 2.5z" fill="none" stroke="#52cf4d" stroke-width="1.5" stroke-linejoin="round"/></svg>
        <svg viewBox="0 0 16 16" aria-hidden="true"><rect x="1.5" y="3.5" width="13" height="9" fill="#52cf4d"/><path d="M1.5 3.5l6.5 5 6.5-5" fill="none" stroke="#1c1c1c" stroke-width="1.3"/></svg>
        <svg viewBox="0 0 16 16" aria-hidden="true"><g fill="none" stroke="#52cf4d" stroke-width="1.3"><circle cx="8" cy="8" r="6.5"/><ellipse cx="8" cy="8" rx="3" ry="6.5"/><path d="M1.5 8h13M2.5 4.8h11M2.5 11.2h11"/></g></svg>
      </div>
      <p>0491 637 158</p>
      <p>hello@korvelselectrical.example</p>
    </div>

    <div class="social-line"><span class="social-line__dot"></span>korvels electrical</div>

    <div class="front-panel">
      <div class="front-panel__logo">Korvel's Electrical &amp; Solar</div>
      <div class="photo front-panel__photo" role="img" aria-label="Electrician testing a switchboard with a multimeter"></div>

      <div class="emergency">
        <svg viewBox="0 0 92 66" aria-hidden="true">
          <rect x="40" y="2" width="12" height="6" fill="#52cf4d"/>
          <path d="M16 60 A30 30 0 1 1 76 60" fill="none" stroke="#52cf4d" stroke-width="6"/>
          <path d="M34 48l8 8 18-16" fill="none" stroke="#ffffff" stroke-width="4" stroke-linecap="round"/>
        </svg>
        <div class="emergency__text">
          <div class="emergency__hours">24/7</div>
          <div class="emergency__label">EMERGENCY</div>
        </div>
      </div>

      <div class="free-quotes"><span>FREE QUOTES</span></div>

      <div class="credentials">
        <div><span class="label">Owen Korvel</span><br>0491 637 158</div>
        <div><span class="label">Lic No.</span> 582614D<br><span class="label">ABN:</span> 41 927 506 318</div>
      </div>
    </div>
  </section>

  <section class="spread spread--inside">
    <div class="photo work-photo" role="img" aria-label="Electrician wiring a switchboard"></div>
    <div class="work-photo__fade"></div>

    <div class="inside-header">
      <h2 class="services-title">OUR SERVICES</h2>
      <h2 class="licensed-title">LICENSED<br>&amp; INSURED</h2>
    </div>

    <ul class="service-list">
      <li>Led Lighting Upgrades</li>
      <li>Switches &amp; Outlets</li>
      <li>Smoke Alarms</li>
      <li>Fault Finding</li>
      <li>Rewiring</li>
      <li>Switchboard Upgrades</li>
      <li>Data/Tv Cabling</li>
      <li>New Builds</li>
      <li>Bathroom/Kitchen/Laundry Renovations</li>
      <li>Test &amp; Tagging</li>
      <li>All Electrical Maintenance &amp; Repairs.</li>
    </ul>

    <ul class="promise-list">
      <li>FAST RESPONSE TIME</li>
      <li>TRANSPARENT PRICING, NO HIDDEN FEES</li>
      <li>QUALITY WORKMANSHIP GUARANTEED</li>
      <li>24/7 EMERGENCY SERVICE</li>
      <li>TRUSTED BY THE LOCAL COMMUNITY</li>
    </ul>

    <aside class="reviews">
      <div class="review review--one">
        <blockquote>"We recently hired Korvels Electrical and Solar. Great communication throughout quoting and prompt response when engaging to commence work. Workmanship and attention to detail A1."<br>We have found our sparky!"</blockquote>
        <cite>- Bernard</cite>
      </div>
      <div class="review review--two">
        <blockquote>"Owen was fantastic! He quickly solved a big problem for me and was extremely punctual, polite, and patient in answering all my questions. He identified the issue straight away, fixed it efficiently, and even gave me valuable advice for the future. I feel very lucky to have found him and would highly recommend his services!"</blockquote>
        <cite>- Mira</cite>
      </div>
      <div class="review review--three">
        <blockquote>"By far the best in the business. The most professional and reliable service I have received. If you're looking for a knowledgeable and experienced service I would highly recommend to anyone."</blockquote>
        <cite>- Felicity</cite>
      </div>
      <div class="reviews__logo">Korvel's Electrical &amp; Solar</div>
    </aside>
  </section>

</div>
</body>
</html>
```